Company Creation Website Redesign

Firmly789 is an Australian company creation website that specialises in creating company and trust documents. Our website was created in 2014 and we would like a new fresh look. We would like to maintain the same colour scheme of light blue and white. We feel the current landing page is a bit busy and would like something cleaner and more minimalist.

We would like all toolbar options to be the same but redesigned with better font, more aesthetically pleasing etc.

The website is built on AngularJS framework with HTML/CSS markup.

Please have a look at the current landing page.
firmly789.com.au

Target Market(s)

Accountants, those want to create company

Industry/Entity Type

Commerce

Coding

Coded - Design and coding required

Number of Pages Required

5+ page

Font styles to use
Sans Serif

Colors
0054AA
0677BA
7BADD7
CADEEF
E8F1F8

Requirements
Must have
• Attractive symbols
Nice to have
• Simple colour scheme
Should not have
• Busy images

```html
<!DOCTYPE html>
<html lang="en">
<head>
<meta charset="utf-8">
<title>Firmly789 – Australian Online Company Registration</title>
<link href="https://fonts.googleapis.com/css2?family=Poppins:ital,wght@0,400;0,500;0,600;0,700;1,500;1,600;1,700;1,800&display=swap" rel="stylesheet">
<style>
:root{
  --navy:#0054aa;
  --blue:#0677ba;
  --sky:#3d8fd6;
  --sky-2:#4a9be0;
  --mid:#7badd7;
  --pale:#cadeef;
  --mist:#e8f1f8;
  --ink:#2b2f36;
  --text:#555b63;
  --white:#ffffff;
  --dark:#1f2328;
  --grey-bg:#eef0f3;
}
*{box-sizing:border-box;margin:0;padding:0}
html,body{width:1200px;height:4474px;overflow:hidden}
body{font-family:"Poppins",sans-serif;color:var(--ink);background:var(--white);position:relative}
section,header,footer{position:absolute;left:0;width:1200px}
.abs{position:absolute}
.italic-head{font-family:"Poppins",sans-serif;font-style:italic;font-weight:700}

/* hero */
.hero{top:0;height:668px;overflow:hidden}
.hero-photo{position:absolute;inset:0;background:linear-gradient(180deg,#2f5f99 0%,#5f7fa6 35%,#8a8676 62%,#5b5442 80%,#2e3438 100%)}
.hero-shade{position:absolute;inset:0;background:linear-gradient(180deg,rgba(10,30,60,.35),rgba(10,20,40,.15) 50%,rgba(10,20,30,.4))}
.brand{left:44px;top:98px;color:var(--white);font-size:24px;font-weight:600;display:flex;align-items:center;gap:10px}
.brand .mark{width:18px;height:18px;background:var(--sky-2);border-radius:3px}
.phone{left:490px;top:38px;color:var(--sky-2);font-size:25px;font-weight:500;display:flex;align-items:center;gap:8px}
.search{left:712px;top:38px;width:278px;height:42px;border:1.5px solid rgba(255,255,255,.7);border-radius:21px;background:rgba(255,255,255,.12);color:rgba(255,255,255,.85);font-size:11px;font-style:italic;padding:13px 14px}
.search svg{position:absolute;right:14px;top:13px}
.login-top{left:1004px;top:36px;width:125px;height:46px;border-radius:23px;background:var(--sky-2);color:var(--white);font-size:15px;font-weight:600;text-align:center;line-height:46px}
.nav{left:254px;top:108px;display:flex;gap:32px;color:var(--white);font-size:12.5px;font-weight:500;letter-spacing:.2px}
.hero h1{position:absolute;left:0;width:1200px;top:262px;text-align:center;color:var(--white);font-size:51px;line-height:58px}
.btn-pill{position:absolute;height:58px;border-radius:29px;color:var(--white);font-style:italic;font-weight:700;font-size:18px;text-align:center;line-height:54px}
.btn-register{left:323px;top:422px;width:226px;background:var(--sky-2);border:2px solid var(--white)}
.btn-update{left:557px;top:422px;width:320px;border:2px solid var(--white);background:rgba(0,0,0,.15)}

/* name check */
.namecheck{top:668px;height:119px;background:var(--sky)}
.namecheck p{position:absolute;left:149px;top:44px;color:var(--white);font-size:23px}
.namecheck .field{left:583px;top:44px;width:341px;height:41px;background:var(--white);border-radius:21px;font-size:11px;font-style:italic;color:#888;padding:13px 20px}
.namecheck .go{left:934px;top:44px;width:115px;height:41px;background:var(--dark);border-radius:21px;color:var(--white);font-size:12px;font-weight:700;font-style:italic;text-align:center;line-height:41px}

/* welcome */
.welcome{top:787px;height:513px}
.welcome .frame{left:156px;top:76px;width:391px;height:295px;border:1.5px solid var(--sky-2)}
.welcome .photo{left:184px;top:107px;width:391px;height:296px;background:linear-gradient(135deg,#9aa5b0,#dfe3e7 45%,#6f7c89)}
.play{left:516px;top:333px;width:104px;height:104px;border-radius:50%;background:var(--sky-2)}
.play svg{position:absolute;left:38px;top:32px}
.welcome h2{position:absolute;left:665px;top:134px;font-size:26px}
.welcome .copy{position:absolute;left:669px;top:183px;width:395px;font-size:13.5px;line-height:21.3px;color:var(--text)}
.btn-small{position:absolute;height:38px;border-radius:19px;background:var(--sky-2);color:var(--white);font-size:12.5px;font-weight:700;font-style:italic;text-align:center;line-height:38px}
.welcome .btn-small{left:665px;top:347px;width:124px}

/* steps */
.steps{top:1300px;height:500px;background:linear-gradient(180deg,#eef5fb,var(--mist) 60%,#e1edf8);overflow:hidden}
.steps h2{position:absolute;left:0;width:1200px;top:66px;text-align:center;font-size:26px;line-height:31px;color:#3a3f46}
.step{position:absolute;top:171px;width:230px;height:230px;border-radius:50%;background:var(--white);box-shadow:0 0 0 8px #e4e7eb}
.step svg.ring{position:absolute;left:-8px;top:-8px}
.step .icon{position:absolute;left:91px;top:42px}
.step .label{position:absolute;left:0;width:230px;top:108px;text-align:center;font-size:14px;line-height:17px;color:#3a3f46}
.step .num{position:absolute;left:0;width:230px;top:172px;text-align:center;font-size:15px;font-weight:700;font-style:italic;color:#8a9099}

/* why */
.why{top:1800px;height:505px;background:var(--sky)}
.why h2{position:absolute;left:149px;top:104px;color:var(--white);font-size:25px}
.why ul{position:absolute;left:155px;top:160px;width:440px;list-style:none;color:var(--white);font-size:13.5px;line-height:16px}
.why li{position:relative;padding-left:25px;margin-bottom:17px}
.why li::before{content:"";position:absolute;left:0;top:1px;width:13px;height:13px;border-radius:50%;background:var(--pale);box-shadow:inset 0 0 0 3px #9cc4e8}
.why .photo{left:653px;top:111px;width:547px;height:394px;background:linear-gradient(120deg,#d8dadb,#f3f2ef 45%,#9b9ea2 75%,#e9e6e1)}

/* testimonials */
.testimonials{top:2305px;height:587px}
.video{left:153px;top:127px;width:503px;height:297px;background:linear-gradient(160deg,#4a3a36,#7c6359 40%,#2d2624)}
.video .title{position:absolute;left:56px;top:16px;color:var(--white);font-size:15px}
.video .badge{position:absolute;left:10px;top:10px;width:36px;height:36px;border-radius:50%;background:var(--white)}
.video .tools{position:absolute;right:10px;top:14px;color:#ddd;font-size:12px;display:flex;gap:20px;text-align:center}
.video .playbtn{position:absolute;left:222px;top:128px;width:60px;height:40px;border-radius:10px;background:rgba(20,20,20,.85)}
.video .playbtn svg{position:absolute;left:23px;top:13px}
.quote-card{left:656px;top:127px;width:400px;height:297px;background:var(--white);box-shadow:0 4px 22px rgba(0,0,0,.12)}
.quote-card h2{position:absolute;left:52px;top:62px;font-size:34px;color:#222}
.quote-card blockquote{position:absolute;left:49px;top:130px;width:300px;font-size:15px;line-height:25px;font-style:italic;color:var(--text)}
.quote-card .who{position:absolute;left:55px;top:222px;font-size:17px;font-weight:600;color:#222}
.quote-card .stars{position:absolute;left:183px;top:220px;color:#f5b100;font-size:19px;letter-spacing:2px}
.arrow{top:270px}

/* update band */
.update{top:2892px;height:351px;background:linear-gradient(160deg,#3f8ed5,#378ad3 60%,#4596dc);overflow:hidden}
.update h2{position:absolute;left:0;width:1200px;top:94px;text-align:center;color:var(--white);font-size:35px;line-height:41px}
.update .btn-outline{position:absolute;left:441px;top:201px;width:318px;height:54px;border:2px solid var(--white);border-radius:27px;color:var(--white);font-size:15px;font-weight:700;font-style:italic;text-align:center;line-height:50px}

/* contact */
.contact{top:3243px;height:479px;background:var(--grey-bg)}
.contact .photo{left:0;top:0;width:600px;height:479px;background:linear-gradient(120deg,#f2efe9,#dcd7cf 50%,#bfb8ad 80%,#e6e2dc)}
.contact h2{position:absolute;left:630px;top:68px;font-size:35px;color:#111}
.contact .rule{left:632px;top:133px;width:80px;height:4px;background:var(--sky-2);border-radius:2px}
.input{position:absolute;height:40px;background:var(--white);border:1px solid #e3e5e8;font-size:13.5px;color:#444;padding:11px 13px}
.contact .submit{left:630px;top:366px;width:119px;height:41px;border-radius:21px;background:var(--sky-2);color:var(--white);font-size:14px;font-weight:600;text-align:center;line-height:41px;box-shadow:0 3px 6px rgba(0,0,0,.15)}

/* sponsors */
.sponsors{top:3722px;height:308px}
.sponsors h2{position:absolute;left:0;width:1200px;top:64px;text-align:center;font-size:35px;color:#111}
.sponsor{position:absolute;top:144px;width:186px;height:96px;background:var(--white);box-shadow:0 2px 12px rgba(0,0,0,.1);display:flex;align-items:center;justify-content:center;gap:8px;font-size:19px;font-weight:600;color:#222}
.sponsor .sq{width:18px;height:18px;background:#222}
.sponsor .ci{width:20px;height:20px;border-radius:50%;background:#222}

/* footer */
.site-footer{top:4030px;height:444px;background:linear-gradient(160deg,#3a8ad2,#3383cc 50%,#3d8fd7);color:var(--white)}
.foot-brand{left:150px;top:204px;font-size:27px;font-weight:600;font-style:italic;display:flex;align-items:center;gap:10px}
.foot-brand .mark{width:22px;height:22px;background:var(--white);border-radius:4px}
.foot-url{left:150px;top:256px;font-size:14px;font-weight:600;font-style:italic}
.foot-call{left:148px;top:282px;font-size:19px;font-weight:700}
.site-footer h3{position:absolute;font-size:19px;font-weight:600;top:96px}
.links{position:absolute;top:137px;font-size:10px;line-height:20px;list-style:none}
.site-footer .input{border:none;font-size:11px;height:40px;padding:12px}
.foot-login{left:766px;top:243px;width:269px;height:40px;background:var(--dark);font-size:14px;font-weight:600;text-align:center;line-height:40px}
.socials{left:167px;top:367px;display:flex;gap:8px}
.socials span{width:37px;height:37px;border:1.5px solid var(--white);border-radius:50%;display:flex;align-items:center;justify-content:center;font-size:11px;font-weight:600}
.legal{left:490px;top:378px;display:flex;gap:42px;font-size:12px}
</style>
</head>
<body>

<header class="hero">
  <div class="hero-photo" role="img" aria-label="Melbourne city skyline at dusk with cathedral spires and a river bridge"></div>
  <div class="hero-shade"></div>
  <div class="abs brand"><span class="mark"></span>Firmly789</div>
  <div class="abs phone">
    <svg width="24" height="24" viewBox="0 0 24 24"><path fill="#4a9be0" d="M6.6 10.8a15.2 15.2 0 0 0 6.6 6.6l2.2-2.2c.3-.3.7-.4 1-.2 1.1.4 2.3.6 3.6.6.6 0 1 .4 1 1V20c0 .6-.4 1-1 1A17 17 0 0 1 3 4c0-.6.4-1 1-1h3.5c.6 0 1 .4 1 1 0 1.3.2 2.5.6 3.6.1.3 0 .7-.2 1z"/></svg>
    03 9000 4127
  </div>
  <div class="abs search">Enter keyword
    <svg width="13" height="13" viewBox="0 0 14 14"><circle cx="6" cy="6" r="4.5" fill="none" stroke="#fff" stroke-width="1.8"/><path d="M9.4 9.4 13 13" stroke="#fff" stroke-width="1.8"/></svg>
  </div>
  <div class="abs login-top">LOGIN</div>
  <nav class="abs nav">
    <span>REGISTER COMPANY</span><span>BUSINESS NAME</span><span>SET UP TRUST</span><span>SET UP BUSINESS PLAN</span><span>REGISTER TRADE MARK</span><span>MORE &#8964;</span>
  </nav>
  <h1 class="italic-head">Australian Online<br>Company Registration</h1>
  <div class="btn-pill btn-register">REGISTER NOW</div>
  <div class="btn-pill btn-update">UPDATE COMPANY DETAILS</div>
</header>

<section class="namecheck">
  <p class="italic-head" style="font-weight:600">Check if company name is available</p>
  <div class="abs field">Company name</div>
  <div class="abs go">CHECK NOW</div>
</section>

<section class="welcome">
  <div class="abs frame"></div>
  <div class="abs photo" role="img" aria-label="Hands joining white jigsaw puzzle pieces"></div>
  <div class="abs play"><svg width="34" height="40" viewBox="0 0 34 40"><path d="M0 0 34 20 0 40z" fill="#fff"/></svg></div>
  <h2 class="italic-head" style="font-weight:600">Welcome to Firmly789</h2>
  <p class="copy">We offer a fully automated, quick and cost effective company registration process. By completing an easy form, within 5 minutes you will receive full company registration documents setting up an Australian private company. We offer full customer support (telephone and email) 24 hours a day. It could not be any simpler, register your company today.</p>
  <div class="btn-small">READ MORE</div>
</section>

<section class="steps">
  <h2 class="italic-head" style="font-weight:600">Simple, quick and trusted<br>service in 3 easy online steps</h2>

  <div class="step" style="left:217px">
    <svg class="ring" width="246" height="246" viewBox="0 0 246 246"><path d="M12 123 A111 111 0 0 0 123 234" fill="none" stroke="#3d8fd6" stroke-width="6"/></svg>
    <svg class="icon" width="48" height="48" viewBox="0 0 48 48" fill="none" stroke="#3d8fd6" stroke-width="2.4"><rect x="6" y="5" width="28" height="38" rx="2"/><path d="M12 15h16M12 22h14M12 29h8"/><path d="M42 16 26 36l-5 2 1-5 16-20z"/></svg>
    <div class="label">Fill in a<br>short form</div>
    <div class="num">Step1</div>
  </div>
  <div class="step" style="left:483px">
    <svg class="ring" width="246" height="246" viewBox="0 0 246 246"><path d="M12 123 A111 111 0 0 1 123 12" fill="none" stroke="#3d8fd6" stroke-width="6"/><path d="M123 234 A111 111 0 0 1 60 214" fill="none" stroke="#3d8fd6" stroke-width="6"/></svg>
    <svg class="icon" width="48" height="48" viewBox="0 0 48 48" fill="none" stroke="#3d8fd6" stroke-width="2.4"><path d="M24 4a20 20 0 1 1-18 11"/><path d="M24 12v12l8 5"/><path d="M4 9l2 7 7-2"/></svg>
    <div class="label">Company<br>registered in less<br>than 5 minutes</div>
    <div class="num">Step2</div>
  </div>
  <div class="step" style="left:747px">
    <svg class="ring" width="246" height="246" viewBox="0 0 246 246"><path d="M12 123 A111 111 0 0 1 123 12" fill="none" stroke="#3d8fd6" stroke-width="6"/><path d="M234 123 A111 111 0 0 1 123 234" fill="none" stroke="#3d8fd6" stroke-width="6"/></svg>
    <svg class="icon" width="52" height="48" viewBox="0 0 52 48" fill="none" stroke="#3d8fd6" stroke-width="2.4"><rect x="4" y="32" width="7" height="12"/><rect x="15" y="24" width="7" height="20"/><rect x="26" y="18" width="7" height="26"/><rect x="37" y="28" width="7" height="16"/><path d="M4 24 18 12l8 6 14-14"/><path d="M34 4h6v6"/><text x="42" y="12" font-size="11" fill="#3d8fd6" stroke="none" font-family="Poppins,sans-serif">$</text></svg>
    <div class="label">Start trading<br>using your company</div>
    <div class="num">Step3</div>
  </div>
</section>

<section class="why">
  <h2 class="italic-head">Why Use Us</h2>
  <ul>
    <li>Quick and simple registration process.</li>
    <li>Company registered in less than 5 minutes.</li>
    <li>Full documentation emailed to you so you can start trading.</li>
    <li>ASIC agent 40927.</li>
    <li>Prepared by a qualified lawyer and accountant.</li>
    <li>Full telephone and email customer support available 24 hours a day.</li>
    <li>The simplest and most cost effective company registration process available.</li>
  </ul>
  <div class="abs photo" role="img" aria-label="Smiling business team in a bright meeting room"></div>
</section>

<section class="testimonials">
  <svg class="abs arrow" style="left:86px" width="20" height="32" viewBox="0 0 20 32"><path d="M16 2 4 16l12 14" fill="none" stroke="#222" stroke-width="2.5"/></svg>
  <svg class="abs arrow" style="left:1110px" width="20" height="32" viewBox="0 0 20 32"><path d="M4 2l12 14L4 30" fill="none" stroke="#222" stroke-width="2.5"/></svg>
  <div class="abs video" role="img" aria-label="Video still of a small business owner speaking about the service">
    <span class="badge"></span>
    <span class="title">Small Business Owner Testimonials: P...</span>
    <span class="tools"><span>Watch Later</span><span>Share</span></span>
    <span class="playbtn"><svg width="14" height="15" viewBox="0 0 14 15"><path d="M0 0 14 7.5 0 15z" fill="#fff"/></svg></span>
  </div>
  <div class="abs quote-card">
    <h2 class="italic-head">Testimonials</h2>
    <blockquote>“I was surprised how easy and quick the process was. Great service at a fantastic price. Thank you”</blockquote>
    <div class="who">Owen Harlow</div>
    <div class="stars">★★★★★</div>
  </div>
</section>

<section class="update">
  <h2 class="italic-head" style="font-weight:600">Update your company<br>changes to ASIC for just $60</h2>
  <div class="btn-outline">UPDATE COMPANY DETAILS</div>
</section>

<section class="contact">
  <div class="abs photo" role="img" aria-label="Woman working on a laptop at a desk"></div>
  <h2 class="italic-head">Contact</h2>
  <div class="abs rule"></div>
  <div class="input" style="left:630px;top:158px;width:214px">Name</div>
  <div class="input" style="left:853px;top:158px;width:217px">Email</div>
  <div class="input" style="left:630px;top:213px;width:214px">Phone</div>
  <div class="input" style="left:853px;top:213px;width:217px">Subject</div>
  <div class="input" style="left:630px;top:271px;width:440px;height:73px">Phone</div>
  <div class="abs submit">Submit</div>
</section>

<section class="sponsors">
  <h2 class="italic-head">List of sponsors</h2>
  <div class="sponsor" style="left:186px"><span class="ci"></span>Staynest</div>
  <div class="sponsor" style="left:400px">Brightreach</div>
  <div class="sponsor" style="left:613px"><span class="sq"></span>Tillbox</div>
  <div class="sponsor" style="left:827px">Halden Finance</div>
</section>

<footer class="site-footer">
  <div class="abs foot-brand"><span class="mark"></span>Firmly789</div>
  <div class="abs foot-url">www.firmly789.com.au</div>
  <div class="abs foot-call">CALL: 03 9000 4127</div>

  <h3 style="left:438px">QUICK LINKS</h3>
  <ul class="links" style="left:438px">
    <li>Set up company</li><li>Business name</li><li>set up trust</li><li>Set up business plan</li><li>Register trademark</li><li>SMSF</li><li>Property withholding</li>
  </ul>
  <ul class="links" style="left:582px">
    <li>clearance certificate</li><li>ABN registration</li><li>Legal &amp; tax consultation</li><li>Pricing</li><li>Resources</li>
  </ul>

  <h3 style="left:766px">CLIENT LOG IN</h3>
  <div class="input" style="left:766px;top:142px;width:269px">Name:</div>
  <div class="input" style="left:766px;top:192px;width:269px">Email:</div>
  <div class="abs foot-login">LOGIN</div>

  <div class="abs socials"><span>Nt</span><span>Bg</span><span>Ch</span><span>Vd</span></div>
  <div class="abs legal"><span>© 2022 All Rights Reserved.</span><span>User Agreement</span><span>Privacy Policy</span><span>Cookie Policy</span></div>
</footer>

</body>
</html>
```